Gilt Corner Shop Sign

Name of company
Gilt Corner
Gilt Corner is a picture framing shop and art gallery selling custom frames, art work and gifts.
Needing a design for shop front sign.

The Sign
The sign is above the shop front window and is approximately 12 feet wide by 43 inches high. White on black. White striped boarder that looks like a picture frame with Gilt Corner in classic lettering including space for a phone number and it may or may not need to include description of services. Something cute in one area like a picture frame with a heart inside. A friendly feel like something that would be special and feels like yours. I have attached a photo of the existing sign to be replaced.

Thank you for your time.

```html
<!DOCTYPE html>
<html lang="en">
<head>
<meta charset="utf-8">
<title>Gilt Corner Shop Sign</title>
<link rel="stylesheet" href="https://fonts.googleapis.com/css2?family=Bodoni+Moda:opsz,wght@6..96,400;6..96,500;6..96,700&display=swap">
<style>
  :root {
    --ink: #000000;
    --paper: #ffffff;
    --line: #e8e8e8;
  }
  * { margin: 0; padding: 0; box-sizing: border-box; }
  html, body {
    width: 1007px;
    height: 1200px;
    overflow: hidden;
    background: var(--ink);
  }
  .canvas {
    position: relative;
    width: 1007px;
    height: 1200px;
    background: var(--ink);
  }
  .sign {
    position: absolute;
    left: 137px;
    top: 497px;
    width: 731px;
    height: 206px;
    background: var(--ink);
  }
  .sign-frame {
    position: absolute;
    inset: 0;
    width: 100%;
    height: 100%;
  }
  .corner-flourish {
    position: absolute;
    width: 30px;
    height: 30px;
    background: var(--paper);
    border-radius: 3px;
  }
  .corner-flourish.top-left { left: 0; top: 0; }
  .corner-flourish.top-right { right: 0; top: 0; }
  .corner-flourish.bottom-left { left: 0; bottom: 0; }
  .corner-flourish.bottom-right { right: 0; bottom: 0; }
  .shop-name {
    position: absolute;
    left: 0;
    right: 0;
    top: 22px;
    text-align: center;
    font-family: "Bodoni Moda", "Didot", serif;
    font-weight: 500;
    font-size: 118px;
    line-height: 1;
    letter-spacing: -1px;
    color: var(--paper);
  }
  .services,
  .phone {
    position: absolute;
    top: 161px;
    font-family: "Bodoni Moda", "Didot", serif;
    font-weight: 700;
    font-size: 17px;
    line-height: 1;
    color: var(--paper);
    letter-spacing: 0.2px;
  }
  .services { left: 53px; }
  .phone { left: 487px; }
</style>
</head>
<body>
<main class="canvas">
  <section class="sign" aria-label="Gilt Corner shop front sign">
    <svg class="sign-frame" viewBox="0 0 731 206" aria-hidden="true">
      <rect x="3" y="3" width="725" height="200" fill="none" stroke="var(--line)" stroke-width="2.5"/>
      <rect x="13" y="13" width="705" height="180" fill="none" stroke="var(--line)" stroke-width="1.5"/>
    </svg>
    <div class="corner-flourish top-left" role="img" aria-label="Decorative corner flourish"></div>
    <div class="corner-flourish top-right" role="img" aria-label="Decorative corner flourish"></div>
    <div class="corner-flourish bottom-left" role="img" aria-label="Decorative corner flourish"></div>
    <div class="corner-flourish bottom-right" role="img" aria-label="Decorative corner flourish"></div>
    <h1 class="shop-name">Gilt Corner</h1>
    <p class="services">FRAMING SHOP AND ART GALLERY</p>
    <p class="phone">T: 01632 960418</p>
  </section>
</main>
</body>
</html>
```